Wordpress Design Project

We are a local restaurant who needs a quality online identity base. We operate in a 1930's Villa, and our target market is the below mid - upper. Our main sale is the evening dinner meal, while we also sell home-made goods, including preserves, and handmade chocolates.
The final Wordpress coded design will:
Be a base for information including Contact details, and a Map of it's location. It will also include photographs of some of the dishes to give an idea to potential customers as to the style and target market.
The site will have 4 main pages
-Main
-About
-Menu
-Contact
Ideas for elements we would like to have included in the design are
Cardboard tags with the links to the other pages, which give a home-made feel
Character wood, with deep grain to emphasis our homely feel
An 'aged' map of the location. Possibly on a large cardboard tag.
Link to our Friendbook page
Link to our Plate Finder review page http://www.platefinder.co.nz/restaurant.php?rest=4273
Notes:
The final Wordpress site should communicate a homely inviting image, with deep character, while still looking elegant and slightly simplistic. We would like fine fonts, with nice spacing, especially on the cardboard tags.
I have attached a mockup of our very loose vision for the site to give you an idea of the line we would like to go down. This is just for initial ideas, and we are happy for radically different designs, or just neat variations on the base design
Professional, edited photos of the food available will be uploaded alongside this project
Villa Rosmar does not have an official Logo for use on the website, so a simple header that ties in with the page will be fine. This may be replaced eventually with a new logo
Address and Hosting is already setup with the address being www.villarosmarresturant.co.nz with a placeholder site online.
We look forward to all designs, and welcome any questions. This should be an nice job for someone with an eye for detail.

```html
<!DOCTYPE html>
<html lang="en">
<head>
<meta charset="utf-8">
<title>Villa Rosmar – The Restaurant</title>
<link rel="stylesheet" href="https://fonts.googleapis.com/css2?family=Questrial&family=Arimo:wght@400&family=Parisienne&display=swap">
<style>
  :root {
    --wood-dark: #4a3324;
    --wood-mid: #7a5a43;
    --wood-light: #9a7a5e;
    --board: #3b2417;
    --board-edge: #7c5638;
    --cream: #f3e4c6;
    --tag: #e8cfa2;
    --tag-dark: #c9a676;
    --ink: #3a2616;
    --page: #161616;
    --page-edge: #6b5441;
    --orange: #c8650f;
    --heading: #d9d9d9;
    --body: #bdbdbd;
    --footer: #2a1d14;
    --white: #ffffff;
    --button: #f2a93a;
  }
  * { margin: 0; padding: 0; box-sizing: border-box; }
  html, body { width: 1200px; height: 1061px; overflow: hidden; }
  body { position: relative; font-family: "Arimo", Arial, sans-serif; background: var(--wood-dark); }

  .wood {
    position: absolute; inset: 0 0 61px 0;
    background:
      repeating-linear-gradient(90deg, rgba(0,0,0,.35) 0 3px, transparent 3px 132px),
      linear-gradient(90deg, var(--wood-mid), var(--wood-light) 25%, var(--wood-mid) 50%, var(--wood-light) 75%, var(--wood-mid));
  }

  .location-button {
    position: absolute; left: 1008px; top: -6px; width: 180px; height: 49px;
    background: linear-gradient(#ffd27a, var(--button));
    border: 2px solid #b36f12; border-radius: 8px;
    display: flex; align-items: center; justify-content: center; gap: 8px;
    font-family: "Questrial", sans-serif; font-size: 20px; letter-spacing: 1px;
    color: var(--ink); text-decoration: none; padding-top: 6px;
  }

  .chain { position: absolute; top: 0; width: 4px; height: 110px; background: repeating-linear-gradient(#d8d8d8 0 8px, #8c8c8c 8px 12px); }

  .signboard {
    position: absolute; left: 362px; top: 94px; width: 495px; height: 126px;
    background: linear-gradient(var(--board), #2a180e);
    border: 4px solid var(--board-edge); border-radius: 10px;
    text-align: center;
  }
  .brand-name {
    font-family: "Questrial", sans-serif; font-size: 54px; color: var(--cream);
    line-height: 1; margin-top: 22px; font-weight: 400;
  }
  .brand-tagline {
    position: absolute; right: 44px; bottom: 8px;
    font-family: "Questrial", sans-serif; font-size: 15px; letter-spacing: 1px; color: var(--cream);
  }

  .tag-string { position: absolute; left: 0; top: 0; }
  .nav-tags { position: absolute; left: 0; top: 0; list-style: none; }
  .nav-tag {
    position: absolute; height: 76px; display: flex; align-items: center; justify-content: center;
    background: linear-gradient(var(--tag), var(--tag-dark));
    border-radius: 6px; box-shadow: 0 3px 6px rgba(0,0,0,.45);
    font-family: "Parisienne", cursive; font-size: 36px; color: var(--ink); text-decoration: none;
  }
  .nav-tag::before, .nav-tag::after {
    content: ""; position: absolute; top: 50%; width: 10px; height: 10px; margin-top: -5px;
    border-radius: 50%; background: var(--wood-dark);
  }
  .nav-tag::before { left: 8px; }
  .nav-tag::after { right: 8px; }

  .book { position: absolute; left: 0; top: 0; }
  .photo-page { position: absolute; left: 0; top: 0; }

  .page-content { position: absolute; left: 673px; top: 432px; width: 437px; }
  .welcome-title {
    font-family: "Questrial", sans-serif; font-size: 24px; font-weight: 400; color: var(--heading);
    padding-bottom: 6px; border-bottom: 5px dashed #4a4a4a; width: 372px; line-height: 1.3;
  }
  .welcome-title span, .category-title { color: var(--orange); }
  .intro {
    margin-top: 12px; font-size: 13.8px; line-height: 26.4px; color: var(--body);
    text-align: justify; hyphens: auto; -webkit-hyphens: auto;
  }
  .category-title { font-family: "Questrial", sans-serif; font-size: 24px; font-weight: 400; margin-top: 10px; }

  .dish-thumb {
    position: absolute; left: 703px; top: 774px; width: 124px; height: 128px;
    border: 3px solid #555; border-radius: 8px;
    background: linear-gradient(160deg, #6a4a30, #b89a78 55%, #4a2e1c);
  }
  .dish-card { position: absolute; left: 852px; top: 748px; width: 270px; }
  .dish-title {
    font-family: "Questrial", sans-serif; font-size: 23px; font-weight: 400; color: var(--heading);
    padding-bottom: 8px; border-bottom: 1px solid #3a3a3a;
  }
  .dish-text { margin-top: 12px; width: 220px; font-size: 14px; line-height: 18px; color: var(--body); }
  .dish-more { margin-top: 10px; font-size: 14px; color: var(--body); }
  .slider-arrow { position: absolute; top: 818px; }

  .site-footer {
    position: absolute; left: 0; bottom: 0; width: 1200px; height: 61px;
    background: linear-gradient(#3a291d, var(--footer));
    color: var(--white); font-size: 14.4px;
  }
  .copyright { position: absolute; left: 56px; top: 24px; }
  .footer-nav { position: absolute; left: 434px; top: 24px; display: flex; gap: 10px; }
  .footer-nav a { color: var(--white); text-decoration: none; }
  .footer-nav .sep { color: var(--white); }
  .social-button {
    position: absolute; right: 40px; top: 8px; height: 45px;
    display: flex; align-items: center; gap: 8px; white-space: nowrap;
    font-family: "Questrial", sans-serif; font-size: 15px; color: var(--tag);
    text-decoration: none;
  }
  .social-square { width: 42px; height: 42px; background: #5a2c1d; border-radius: 3px; flex: none; }
</style>
</head>
<body>
  <div class="wood" role="img" aria-label="Background of weathered vertical wooden planks with deep grain"></div>

  <a class="location-button" href="#contact">
    <svg width="22" height="22" viewBox="0 0 24 24" aria-hidden="true"><path d="M12 2a7 7 0 0 0-7 7c0 5 7 13 7 13s7-8 7-13a7 7 0 0 0-7-7z" fill="#2f6b3a"/><circle cx="12" cy="9" r="2.6" fill="#ffd27a"/></svg>
    LOCATION
  </a>

  <span class="chain" style="left:388px"></span>
  <span class="chain" style="left:826px"></span>

  <header class="signboard">
    <h1 class="brand-name">Villa Rosmar</h1>
    <p class="brand-tagline">THE RESTAURANT</p>
  </header>

  <svg class="tag-string" width="1200" height="400" aria-hidden="true">
    <polyline points="258,290 300,292 440,300 600,302 760,312 942,316" fill="none" stroke="#cfc3b0" stroke-width="3"/>
    <circle cx="258" cy="290" r="5" fill="#2a1a10"/><circle cx="942" cy="316" r="5" fill="#2a1a10"/>
  </svg>

  <nav>
    <ul class="nav-tags">
      <li><a class="nav-tag" href="#home" style="left:288px;top:268px;width:138px;transform:rotate(5deg)">home</a></li>
      <li><a class="nav-tag" href="#about" style="left:444px;top:276px;width:134px;transform:rotate(-3deg)">about</a></li>
      <li><a class="nav-tag" href="#menu" style="left:598px;top:280px;width:138px;transform:rotate(6deg)">menu</a></li>
      <li><a class="nav-tag" href="#contact" style="left:752px;top:284px;width:152px;transform:rotate(-4deg)">contact</a></li>
    </ul>
  </nav>

  <svg class="photo-page" width="1200" height="1061" role="img" aria-label="Photograph of candle-lit glass votive holders glowing in the evening">
    <defs>
      <linearGradient id="candleGlow" x1="0" y1="0" x2="1" y2="1">
        <stop offset="0" stop-color="#3b4a52"/>
        <stop offset=".45" stop-color="#8a5a2e"/>
        <stop offset=".7" stop-color="#d9a35c"/>
        <stop offset="1" stop-color="#3a2418"/>
      </linearGradient>
    </defs>
    <path d="M70,372 C200,352 420,392 600,366 L600,972 C420,948 200,984 70,966 Q58,962 58,948 L58,390 Q58,376 70,372 Z" fill="url(#candleGlow)" stroke="var(--page-edge)" stroke-width="5"/>
  </svg>

  <svg class="book" width="1200" height="1061" aria-hidden="true">
    <path d="M612,366 C780,394 1000,346 1144,370 Q1158,374 1158,390 L1158,946 Q1158,962 1144,964 C1000,984 780,946 612,972 Z" fill="var(--page)" stroke="var(--page-edge)" stroke-width="5"/>
    <g fill="#111" stroke="#8a7560" stroke-width="3">
      <circle cx="584" cy="428" r="5"/><circle cx="584" cy="476" r="5"/><circle cx="584" cy="524" r="5"/>
      <circle cx="584" cy="572" r="5"/><circle cx="584" cy="620" r="5"/><circle cx="584" cy="668" r="5"/>
      <circle cx="584" cy="716" r="5"/><circle cx="584" cy="764" r="5"/><circle cx="584" cy="812" r="5"/>
      <circle cx="584" cy="860" r="5"/><circle cx="584" cy="908" r="5"/>
    </g>
    <g stroke="#9c8668" stroke-width="3">
      <line x1="589" y1="428" x2="626" y2="428"/><line x1="589" y1="476" x2="626" y2="476"/><line x1="589" y1="524" x2="626" y2="524"/>
      <line x1="589" y1="572" x2="626" y2="572"/><line x1="589" y1="620" x2="626" y2="620"/><line x1="589" y1="668" x2="626" y2="668"/>
      <line x1="589" y1="716" x2="626" y2="716"/><line x1="589" y1="764" x2="626" y2="764"/><line x1="589" y1="812" x2="626" y2="812"/>
      <line x1="589" y1="860" x2="626" y2="860"/><line x1="589" y1="908" x2="626" y2="908"/>
    </g>
    <g fill="#111">
      <circle cx="630" cy="428" r="5"/><circle cx="630" cy="476" r="5"/><circle cx="630" cy="524" r="5"/>
      <circle cx="630" cy="572" r="5"/><circle cx="630" cy="620" r="5"/><circle cx="630" cy="668" r="5"/>
      <circle cx="630" cy="716" r="5"/><circle cx="630" cy="764" r="5"/><circle cx="630" cy="812" r="5"/>
      <circle cx="630" cy="860" r="5"/><circle cx="630" cy="908" r="5"/>
    </g>
  </svg>

  <main class="page-content">
    <h2 class="welcome-title">Welcome to <span>Villa Rosmar</span></h2>
    <p class="intro">Lorem ipsum dolor sit amet, consectetur adipiscing elit. Nullam ultri&shy;cies commodo semper. In volutpat, risus a pretium fringilla, mauris elit tempus eros, non porta lorem ipsum non tortor. Sed dapibus adipiscing massa, ac dictum nunc tempus sed. Nulla facilisi. Fusce blandit sapien non risus blandit laoreet varius nec nisi. Vestibulum ante ipsum primis in faucibus orci luctus et ultrices posuere cubilia Curae; Maecenas laoreet lorem vel ipsum malesuada vel iaculis ante iaculis. Morbi vitae nisi quis dui gravida faucibus.</p>
    <h3 class="category-title">Category</h3>
  </main>

  <svg class="slider-arrow" style="left:660px" width="16" height="40" aria-hidden="true"><path d="M13,2 L3,20 L13,38" fill="none" stroke="#b07a6a" stroke-width="3"/></svg>
  <svg class="slider-arrow" style="left:1106px" width="16" height="40" aria-hidden="true"><path d="M3,2 L13,20 L3,38" fill="none" stroke="#b07a6a" stroke-width="3"/></svg>

  <div class="dish-thumb" role="img" aria-label="Photograph of a chocolate dessert with ice cream"></div>

  <article class="dish-card">
    <h4 class="dish-title">Chocolates</h4>
    <p class="dish-text">Lorem ipsum dolor sit amet, consectetur adipiscing elit. Nullam ultricies commodo semper.</p>
    <p class="dish-more">Loremipadcing Lorem...</p>
  </article>

  <footer class="site-footer">
    <p class="copyright">All Rights Reserved@Villarosmar</p>
    <nav class="footer-nav">
      <a href="#home">Home</a><span class="sep">|</span>
      <a href="#about">About</a><span class="sep">|</span>
      <a href="#menu">Menu</a><span class="sep">|</span>
      <a href="#terms">Terms</a><span class="sep">|</span>
      <a href="#contact">Contact us</a>
    </nav>
    <a class="social-button" href="#friendbook">VISIT US ON FRIENDBOOK <span class="social-square"></span></a>
  </footer>
</body>
</html>
```